依頼詳細
ロゴはミナモワークスで作成していただいていますので、それを使用していただいきたいです。ホームページは現在作成中です。ロゴを取り入れ、柔らかい雰囲気でシンプルなイメージ、わかりやすい感じがいいです。
記載項目
病院名、ロゴ、開業日、内覧会の日程、住所、電話番号、ホームページのアドレス、診察時間、休診日 対象動物、挨拶等
サイズ
A4
ページ数
片面
希望イメージ
シンプル 複雑
単色 カラフル
暗い 明るい
日常 高級
遊び心 厳粛
未来的 伝統的
女性的 男性的
希望する色
納品ファイル
補足説明
ロゴを添付します。

挨拶内容
「はじめまして、はるかぜペットクリニック院長の森岡健司です。大学卒業後、熊本市内の動物病院で7年間勤務し、2014年3月24日に動物病院を開院することになりました。
ホームドクターとして地域の皆様に親しまれる病院であるとともに、飼い主様と一緒に家族である動物たちの最善のケアができるように努めてまいりたいと思います。ワンちゃん達が遊べるスペースも少しですが用意してあります。ぜひ気軽に遊びにいらしてください。今後ともよろしくお願い致します。」
おそくなりましたが、ホームページのドメイン決まりました。
http://harukaze-petclinic.exampleです。
よろしくお願いいたします。
■ 選んだ理由

シンプルで開院ということがわかりやすかったため。
犬の写真の雰囲気も良かったです。

■ 提案者全員のお礼・コメント

いいデザインを多数いただいてありがとうございます。それぞれおもしろくけっこう悩ませていただきました。また、よろしくお願いいたします。

```html
<!DOCTYPE html>
<html lang="ja">
<head>
<meta charset="utf-8">
<title>はるかぜペットクリニック 開院のお知らせ</title>
<link rel="stylesheet" href="https://fonts.googleapis.com/css2?family=M+PLUS+Rounded+1c:wght@400;500;700;800&display=swap">
<style>
:root{
  --blue:#1f6fb8;
  --blue-deep:#175a99;
  --orange:#f0a11e;
  --ink:#4a4a4a;
  --paper:#ffffff;
  --sky-top:#e9f3fb;
  --photo-light:#efe6d8;
  --photo-mid:#c9a77c;
  --photo-dark:#8a6a48;
}
*{margin:0;padding:0;box-sizing:border-box}
html,body{width:846px;height:1200px;overflow:hidden;background:var(--paper)}
body{font-family:"M PLUS Rounded 1c",sans-serif;color:var(--ink)}
.poster{position:relative;width:846px;height:1200px;background:linear-gradient(180deg,var(--paper) 0%,var(--paper) 60%,var(--sky-top) 70%,var(--paper) 80%);overflow:hidden}

.brand{position:absolute;top:70px;left:0;width:100%;text-align:center;color:var(--blue);font-weight:700}
.brand-mark{display:block;width:96px;height:96px;margin:0 auto 26px;border-radius:50%;background:var(--blue)}
.brand-name{display:block;font-size:46px;letter-spacing:2px;line-height:1.1}
.brand-sub{display:block;font-size:26px;margin-top:8px;letter-spacing:1px}

.opening{position:absolute;top:322px;left:0;width:100%;text-align:center}
.opening-date{font-size:54px;font-weight:800;color:var(--blue);letter-spacing:1px}
.opening-date small{font-size:34px}
.opening-word{font-size:138px;font-weight:800;color:var(--orange);letter-spacing:28px;line-height:1.15;margin-left:28px}

.preview{position:absolute;top:330px;left:622px;width:190px;height:190px;border-radius:50%;background:var(--orange);color:#fff;text-align:center;padding-top:26px}
.preview-title{font-size:24px;font-weight:800}
.preview-days{font-size:38px;font-weight:800;line-height:1.2}
.preview-days .dow{display:inline-block;width:22px;height:22px;border-radius:50%;background:#fff;color:var(--orange);font-size:14px;line-height:22px;vertical-align:middle;margin:0 2px}
.preview-time{font-size:16px;font-weight:700}
.preview-note{font-size:13px;margin-top:6px;line-height:1.35}

.greeting{position:absolute;top:592px;left:0;width:100%;text-align:center}
.greeting-title{font-size:16px;font-weight:700;color:var(--blue);letter-spacing:4px;margin-bottom:12px}
.greeting-body{font-size:14.5px;line-height:1.95;font-weight:500}

.photo{position:absolute;top:810px;left:0;width:846px;height:258px;background:radial-gradient(ellipse 46% 70% at 48% 62%,var(--photo-mid) 0%,var(--photo-dark) 45%,rgba(138,106,72,0) 75%),linear-gradient(180deg,rgba(239,230,216,0) 0%,var(--photo-light) 100%)}

.info{position:absolute;top:1068px;left:0;width:846px;height:132px;background:var(--blue);color:#fff;display:flex;align-items:center;padding:0 22px;gap:20px}
.contact{width:260px}
.contact-label{display:inline-block;font-size:12px;background:#fff;color:var(--blue);padding:1px 10px;border-radius:10px;margin-bottom:4px}
.contact-tel{font-size:38px;font-weight:800;line-height:1.1;white-space:nowrap}
.contact-tel small{font-size:22px}
.contact-sub{font-size:12px;line-height:1.6;white-space:nowrap}
.address{font-size:13px;font-weight:500;width:180px;align-self:flex-start;padding-top:20px}
.hours{font-size:12.5px;line-height:1.75;flex:1;white-space:nowrap}
.map{width:110px;height:104px;background:#fff;border-radius:4px}
</style>
</head>
<body>
<main class="poster">
  <header class="brand">
    <span class="brand-mark"></span>
    <span class="brand-name">はるかぜペットクリニック</span>
    <span class="brand-sub">Harukaze Pet Clinic</span>
  </header>

  <section class="opening">
    <p class="opening-date">2014.3.24.<small>mon</small></p>
    <h1 class="opening-word">開院</h1>
  </section>

  <aside class="preview">
    <p class="preview-title">内覧会開催</p>
    <p class="preview-days">3.21<span class="dow">金</span>22<span class="dow">土</span></p>
    <p class="preview-time">10:00～17:00まで</p>
    <p class="preview-note">お気軽にお越し<br>ください</p>
  </aside>

  <section class="greeting">
    <h2 class="greeting-title">ごあいさつ</h2>
    <p class="greeting-body">
      はじめまして、はるかぜペットクリニック院長の森岡健司です。<br>
      大学卒業後、熊本市内の動物病院で7年間勤務し、2014年3月24日に動物病院を開院することになりました。<br>
      ホームドクターとして地域の皆様に親しまれる病院であるとともに、<br>
      飼い主様と一緒に家族である動物たちの最善のケアができるように努めてまいりたいと思います。<br>
      ワンちゃん達が遊べるスペースも少しですが用意してあります。ぜひ気軽に遊びにいらしてください。<br>
      今後ともよろしくお願い致します。
    </p>
  </section>

  <div class="photo" role="img" aria-label="床に顎をのせてこちらを見上げる小型犬の写真"></div>

  <footer class="info">
    <div class="contact">
      <span class="contact-label">お問い合わせ・ご予約</span>
      <p class="contact-tel"><small>Tel.</small>096-555-0148</p>
      <p class="contact-sub">Fax.096-555-0149　http://harukaze-petclinic.example</p>
    </div>
    <p class="address">熊本市東区若葉台2-8-15</p>
    <div class="hours">
      平日 9:00～12:00 / 15:00～19:30<br>
      土曜 9:00～12:00 / 15:00～18:00<br>
      日曜・祝日休診<br>
      対象動物:犬・猫・ウサギ・ハムスター 等
    </div>
    <div class="map" role="img" aria-label="クリニック周辺の案内地図"></div>
  </footer>
</main>
</body>
</html>
```